Merrow Sailcraft Works President Business Card Carbon fiber catamarans

Hi.. I need a new business card design.. I am the President of a high tech yacht builder. We build Carbon Fiber go fast catamarans... Maybe we use the file I am sharing to you as the back of the card.. We need to look cool and crisp ...

Target Market(s)

Affluent People who will purchase a cool yacht

Industry/Entity Type

Custom Yacht Builder

Contact Information for Business Card

Dale Penwarty , President, 517.608.2391 USA

Font styles to use
Serif

Requirements
Must have
• the clean crisp cool feel
Nice to have
• clean and crisp
Should not have
• Bold ugly

```html
<!DOCTYPE html>
<html lang="en">
<head>
<meta charset="utf-8">
<title>Merrow Sailcraft Works — Business Card</title>
<link rel="stylesheet" href="https://fonts.googleapis.com/css2?family=Michroma&display=swap">
<style>
  :root {
    --page-bg: #e4e4e4;
    --card-dark: #111111;
    --card-mid: #1e1e1e;
    --silver: #cfd0d2;
    --silver-soft: #a9abae;
    --rule: #8e9094;
  }
  * { margin: 0; padding: 0; box-sizing: border-box; }
  html, body {
    width: 1200px;
    height: 1200px;
    overflow: hidden;
    background: var(--page-bg);
  }
  .canvas {
    position: relative;
    width: 1200px;
    height: 1200px;
    font-family: "Michroma", sans-serif;
    color: var(--silver);
  }
  .card {
    position: absolute;
    left: 242px;
    width: 703px;
    height: 400px;
    background: linear-gradient(135deg, var(--card-mid) 0%, var(--card-dark) 55%, var(--card-mid) 100%);
    box-shadow: 0 3px 8px rgba(0, 0, 0, 0.35);
  }
  .card--front { top: 170px; }
  .card--back { top: 629px; }

  .brand {
    position: absolute;
    display: flex;
    align-items: center;
    gap: 14px;
  }
  .brand__dot {
    width: 14px;
    height: 14px;
    border-radius: 50%;
    background: var(--silver);
    flex: none;
  }
  .brand__name {
    font-weight: 400;
    color: var(--silver);
    text-transform: uppercase;
    line-height: 1.35;
  }
  .brand__line { display: block; }

  .card--front .brand {
    right: 30px;
    bottom: 42px;
  }
  .card--front .brand__name { font-size: 21px; letter-spacing: 3px; }
  .card--front .brand__line--small { font-size: 11px; letter-spacing: 3.2px; }

  .card--back .brand {
    right: 420px;
    top: 172px;
    flex-direction: column;
    align-items: center;
    gap: 10px;
    text-align: center;
  }
  .card--back .brand__name { font-size: 12px; letter-spacing: 2.5px; }

  .divider {
    position: absolute;
    left: 330px;
    top: 157px;
    width: 2px;
    height: 94px;
    background: var(--rule);
  }
  .contact {
    position: absolute;
    left: 350px;
    top: 155px;
    text-transform: uppercase;
  }
  .contact__name {
    font-size: 17px;
    letter-spacing: 2.5px;
    line-height: 1;
  }
  .contact__title {
    margin-top: 6px;
    font-size: 10px;
    letter-spacing: 2.5px;
    color: var(--silver-soft);
  }
  .contact__phone {
    margin-top: 25px;
    font-size: 13px;
    letter-spacing: 3px;
  }
  .contact__country {
    margin-top: 8px;
    font-size: 13px;
    letter-spacing: 3px;
  }
</style>
</head>
<body>
<main class="canvas">
  <section class="card card--front" aria-label="Card front">
    <div class="brand">
      <span class="brand__dot"></span>
      <span class="brand__name">
        <span class="brand__line">Merrow</span>
        <span class="brand__line brand__line--small">Sailcraft Works</span>
      </span>
    </div>
  </section>

  <section class="card card--back" aria-label="Card back">
    <div class="brand">
      <span class="brand__dot"></span>
      <span class="brand__name">
        <span class="brand__line">Merrow</span>
        <span class="brand__line">Sailcraft</span>
        <span class="brand__line">Works</span>
      </span>
    </div>
    <div class="divider"></div>
    <div class="contact">
      <p class="contact__name">Dale Penwarty</p>
      <p class="contact__title">President</p>
      <p class="contact__phone">517 · 608 · 2391</p>
      <p class="contact__country">USA</p>
    </div>
  </section>
</main>
</body>
</html>
```